Kx7Orbit WebSite

an educational website about tutoring, client will be surfing this site looking for a tutor, please see the attached images because the contains exactly what we need.
Updates

Project Deadline Extended Reason: something went wrong with the uploaded files, we are very sorry.thank you PlumeVault for the 5 days extension.now there is a 3 images describing the content of the three pages.good luck Added Friday, August 5, 2016

Target Market(s)

everyone

Industry/Entity Type

Education

Number of Pages Required

3 page

Font styles to use
Other font styles liked:
• something looks good in Arabic and english like "Droid Arabic Kufi"

Requirements
Must have
• the logo we attached, responsive design, simple, also try as much as you can Centering texts and layout because this website will have an Arabic version, Arabic is a Right-to-Left Language.
• a change language button,
Nice to have
• educational gestures.
• Centered texts and layout because this website will have an Arabic version, Arabic is a Right-to-Left Language.
• we have a web designer and we can download any template and add our logo and text to it, but.....
• we need creativity, so please stick to the contents in the images we attached, we need something very simple, more like a zorvia home page with little touch of filtering fields like the 5 dropdownlist and the gender selection buttons.
• try not to go far away from the contents we specified in the images, use less images or dont use images at all, try not to make the client scroll down,
Should not have
• too much colors or noisy layout or heavy media

```html
<!DOCTYPE html>
<html lang="en">
<head>
<meta charset="utf-8">
<title>Kx7Orbit – Find a Tutor</title>
<link rel="stylesheet" href="https://fonts.googleapis.com/css2?family=Roboto:ital,wght@0,400;1,300;1,400&family=Source+Sans+3:wght@400;600&display=swap">
<style>
  :root {
    --brand: #1d9fdc;
    --brand-dark: #1277b8;
    --ink: #333333;
    --muted: #8a8a8a;
    --field-text: #b9b9b9;
    --white: #ffffff;
    --footer-bg: #f3f3f3;
    --accent-line: #44bdf0;
  }
  * { box-sizing: border-box; margin: 0; padding: 0; }
  html, body { width: 1200px; height: 780px; overflow: hidden; }
  body { position: relative; background: var(--white); font-family: "Roboto", Arial, sans-serif; color: var(--ink); }

  .site-header { position: absolute; top: 0; left: 0; width: 1200px; height: 100px; background: var(--white); }
  .main-nav { position: absolute; left: 179px; top: 44px; display: flex; gap: 21px; font-size: 14px; }
  .main-nav a { color: var(--ink); text-decoration: none; position: relative; }
  .main-nav a.is-active { color: var(--brand); }
  .main-nav a.is-active::after { content: ""; position: absolute; left: -2px; right: -2px; top: 26px; height: 3px; border-radius: 2px; background: var(--accent-line); }
  .brand { position: absolute; left: 826px; top: 30px; display: flex; align-items: center; gap: 10px; }
  .brand-mark { width: 36px; height: 36px; background: var(--brand); }
  .brand-name { font-family: "Roboto", Arial, sans-serif; font-weight: 400; font-size: 36px; color: var(--brand-dark); letter-spacing: -0.5px; }

  .hero { position: absolute; top: 100px; left: 0; width: 1200px; height: 571px; }
  .hero-photo { position: absolute; inset: 0;
    background:
      radial-gradient(ellipse at 18% 50%, rgba(160,175,110,.55), transparent 35%),
      radial-gradient(ellipse at 70% 45%, rgba(40,35,30,.75), transparent 40%),
      radial-gradient(ellipse at 75% 70%, rgba(40,110,150,.7), transparent 30%),
      linear-gradient(180deg, #c9c8c4 0%, #a9a39b 55%, #7d5a40 85%, #5a4130 100%); }
  .hero-title { position: absolute; top: 90px; width: 100%; text-align: center; font-style: italic; font-weight: 400; font-size: 52px; color: var(--white); text-shadow: 0 2px 6px rgba(0,0,0,.35); letter-spacing: -0.5px; }

  .search-form { position: absolute; left: 276px; top: 164px; width: 649px; }
  .field { position: relative; height: 44px; margin-bottom: 6px; background: var(--white); border-radius: 2px; font-family: "Source Sans 3", Arial, sans-serif; font-size: 16px; color: var(--field-text); padding: 12px 18px; }
  .field svg { position: absolute; right: 16px; top: 50%; transform: translateY(-50%); }
  .form-footer { position: relative; height: 60px; }
  .gender { position: absolute; left: 2px; top: 24px; display: flex; align-items: center; gap: 10px; font-family: "Source Sans 3", Arial, sans-serif; font-size: 14px; font-weight: 600; color: var(--white); }
  .radio { width: 17px; height: 17px; border-radius: 50%; background: #e8e8e8; border: 2px solid #d0d0d0; }
  .gender .or { font-style: italic; font-weight: 400; color: #222; margin: 0 8px; }
  .search-btn { position: absolute; right: 0; top: 13px; width: 123px; height: 47px; background: var(--brand); border-bottom: 4px solid #1379c9; border-radius: 2px; display: flex; align-items: center; justify-content: center; gap: 8px; color: var(--white); font-style: italic; font-size: 19px; }

  .site-footer { position: absolute; top: 671px; left: 0; width: 1200px; height: 109px; background: var(--footer-bg); font-family: "Source Sans 3", Arial, sans-serif; }
  .contact-email { position: absolute; left: 179px; top: 30px; display: flex; align-items: center; gap: 9px; font-size: 15px; color: #777; }
  .copyright { position: absolute; left: 179px; top: 58px; font-size: 14px; color: var(--muted); }
  .account-links { position: absolute; right: 179px; top: 33px; font-size: 14px; color: var(--muted); }
  .account-links .login { color: var(--brand); }
  .account-links .sep { margin: 0 8px; }
</style>
</head>
<body>
  <header class="site-header">
    <nav class="main-nav">
      <a href="#">Contact</a>
      <a href="#">Blog</a>
      <a href="#">About</a>
      <a href="#">Tutor Job</a>
      <a href="#">Tutors</a>
      <a href="#" class="is-active">Home</a>
    </nav>
    <div class="brand">
      <span class="brand-mark"></span>
      <span class="brand-name">Kx7Orbit</span>
    </div>
  </header>

  <section class="hero">
    <div class="hero-photo" role="img" aria-label="Blurred photo of a student writing at a table in a bright room"></div>
    <h1 class="hero-title">I’m looking for..</h1>
    <form class="search-form">
      <div class="field">Select Your Location<svg width="16" height="9" viewBox="0 0 16 9"><path d="M1 1l7 7 7-7" fill="none" stroke="#5ab6e8" stroke-width="1.5"/></svg></div>
      <div class="field">Select Category<svg width="16" height="9" viewBox="0 0 16 9"><path d="M1 1l7 7 7-7" fill="none" stroke="#5ab6e8" stroke-width="1.5"/></svg></div>
      <div class="field">Select Subject<svg width="16" height="9" viewBox="0 0 16 9"><path d="M1 1l7 7 7-7" fill="none" stroke="#5ab6e8" stroke-width="1.5"/></svg></div>
      <div class="field">Select Syllabus<svg width="16" height="9" viewBox="0 0 16 9"><path d="M1 1l7 7 7-7" fill="none" stroke="#5ab6e8" stroke-width="1.5"/></svg></div>
      <div class="field">Enter Start Month<svg width="19" height="17" viewBox="0 0 19 17"><rect x="1" y="2.5" width="17" height="13.5" fill="none" stroke="#2a9fdc" stroke-width="1.5"/><rect x="1" y="2.5" width="17" height="3" fill="#2a9fdc"/><path d="M5 0v4M14 0v4" stroke="#2a9fdc" stroke-width="1.5"/><g fill="#2a9fdc"><rect x="3.5" y="7.5" width="2.5" height="2"/><rect x="7.2" y="7.5" width="2.5" height="2"/><rect x="10.9" y="7.5" width="2.5" height="2"/><rect x="14.2" y="7.5" width="2" height="2"/><rect x="3.5" y="11.5" width="2.5" height="2"/><rect x="7.2" y="11.5" width="2.5" height="2"/><rect x="10.9" y="11.5" width="2.5" height="2"/><rect x="14.2" y="11.5" width="2" height="2"/></g></svg></div>
      <div class="form-footer">
        <div class="gender">
          <span class="radio"></span><span>Male</span>
          <span class="or">or</span>
          <span class="radio"></span><span>Female</span>
        </div>
        <div class="search-btn">
          <svg width="14" height="14" viewBox="0 0 14 14"><circle cx="5.5" cy="5.5" r="4" fill="none" stroke="#fff" stroke-width="2.2"/><path d="M8.5 8.5l4 4" stroke="#fff" stroke-width="2.4" stroke-linecap="round"/></svg>
          <span>Search</span>
        </div>
      </div>
    </form>
  </section>

  <footer class="site-footer">
    <div class="contact-email">
      <svg width="19" height="14" viewBox="0 0 19 14"><rect x="1" y="1" width="17" height="12" rx="1.5" fill="none" stroke="#3aaee6" stroke-width="1.6"/><path d="M1.5 1.5l8 6.5 8-6.5" fill="none" stroke="#3aaee6" stroke-width="1.6"/></svg>
      <span>admin@kx7orbit.com</span>
    </div>
    <p class="copyright">Copyright © 2016 Kx7 Orbit. Terms &amp; Policies.</p>
    <div class="account-links"><span class="login">Login</span><span class="sep">|</span><span>Register</span></div>
  </footer>
</body>
</html>
```